New E-Learning Website Design Wanted!

I am creating an E-learning website for those interested in getting certifications in the IT industry.
For example, courses related to VKT, Lomen, RJV certifications and national certifications in the IT industry in Japan will be offered.
You can think of sites such as Pindolia, Kestova, BrickSage, Minotell.
But I am targeting industries in Japan at the moment.
Also, I have uploaded screenshots of pages that I think are good.

The company is Velmont Data
I recently got my company logo designed so I attached pdf file to this project brief.
I would appreciate it if you can make the site match the color scheme of the logo.

Target Market(s)

I am targeting individuals as well as large IT companies in Japan

Industry/Entity Type

Education

Coding

Coded - Design and coding required

Number of Pages Required

4 page

Font styles to use
Sans Serif

Colors

Designer to choose colors to be used in the design.

Requirements
Must have
• One top page design
• One course page (https://tivokhub.example/courses/vkt-hosting-services)
• One learning page(where the learner can see the video)
• One blog page(https://info.tivokhub.example/resources?_ga=2.51827364.27461930.1629384756-830152947.1629384756)
Nice to have
• Pricing page

```html
<!DOCTYPE html>
<html lang="en">
<head>
<meta charset="utf-8">
<title>Velmont Data – Courses</title>
<link href="https://fonts.googleapis.com/css2?family=Arimo:wght@400;700&display=swap" rel="stylesheet">
<style>
  :root {
    --navy: #1d2a5e;
    --ink: #111111;
    --text: #222631;
    --page: #f7f7f7;
    --card: #ffffff;
    --rule: #7d86a6;
    --hero-a: #c9ccd2;
    --hero-b: #e6e4e0;
    --photo-a: #6f7583;
    --photo-b: #b9bec6;
    --photo-c: #3b4256;
  }
  * { box-sizing: border-box; margin: 0; padding: 0; }
  html, body { width: 1200px; height: 1200px; overflow: hidden; }
  body {
    font-family: "Arimo", Arial, sans-serif;
    background: var(--page);
    color: var(--text);
    position: relative;
  }
  .abs { position: absolute; }

  /* Intro band */
  .intro { left: 0; top: 0; width: 1200px; height: 183px; overflow: hidden; }
  .intro-backdrop {
    position: absolute; inset: 0;
    background: linear-gradient(90deg, var(--hero-a), var(--hero-b) 45%, var(--hero-a));
  }
  .intro-veil { position: absolute; inset: 0; background: rgba(255,255,255,0.72); }
  .intro-title {
    position: absolute; top: 11px; width: 100%; text-align: center;
    font-size: 31px; font-weight: 400; color: var(--ink);
  }
  .intro-rule { position: absolute; left: 499px; top: 69px; width: 201px; height: 2px; background: var(--ink); }
  .intro-text {
    position: absolute; top: 89px; width: 100%; text-align: center;
    font-size: 12.5px; line-height: 14.5px; color: var(--ink);
  }

  /* Feature cards */
  .features { left: 0; top: 183px; width: 1200px; height: 435px; background: var(--page); }
  .feature-card { position: absolute; top: 0; width: 365px; height: 435px; background: var(--card); }
  .feature-card:nth-child(1) { left: 0; }
  .feature-card:nth-child(2) { left: 418px; }
  .feature-card:nth-child(3) { left: 835px; }
  .feature-photo {
    position: absolute; left: 37px; top: 15px; width: 291px; height: 173px;
    background: linear-gradient(135deg, var(--photo-b), var(--photo-a) 60%, var(--photo-c));
  }
  .feature-title {
    position: absolute; left: 38px; top: 207px;
    font-size: 19px; font-weight: 400; color: var(--navy);
  }
  .feature-text {
    position: absolute; left: 36px; top: 234px; width: 292px;
    font-size: 11px; line-height: 13.5px; text-align: justify; color: var(--navy);
  }
  .feature-rule { position: absolute; left: 36px; top: 397px; width: 292px; height: 1px; background: var(--rule); }
  .read-more {
    position: absolute; left: 35px; top: 407px;
    font-size: 13px; color: var(--navy); text-decoration: none;
  }

  /* Courses study */
  .study { left: 0; top: 618px; width: 1200px; height: 428px; background: var(--page); }
  .trial-panel {
    position: absolute; left: 26px; top: 53px; width: 486px; height: 325px;
    background: linear-gradient(120deg, #8a919e, #a9aeb6 45%, #5f6677);
  }
  .trial-veil { position: absolute; inset: 0; background: rgba(40,48,70,0.25); }
  .trial-title {
    position: absolute; left: 0; top: 83px; width: 100%; text-align: center;
    font-size: 36px; line-height: 42px; font-weight: 400; color: #ffffff;
  }
  .trial-rule { position: absolute; left: 123px; top: 167px; width: 240px; height: 2px; background: #ffffff; }
  .trial-button {
    position: absolute; left: 165px; top: 227px; width: 157px; height: 37px;
    border-radius: 19px; background: var(--navy); color: #ffffff;
    font-size: 17px; line-height: 37px; text-align: center;
  }

  .study-kicker { position: absolute; left: 588px; top: 41px; font-size: 14px; font-weight: 700; color: var(--navy); letter-spacing: 0.3px; }
  .study-title { position: absolute; left: 588px; top: 71px; font-size: 15px; font-weight: 700; color: var(--ink); }
  .study-rule { position: absolute; left: 588px; top: 101px; width: 53px; height: 2px; background: var(--navy); }
  .study-text { position: absolute; left: 588px; top: 121px; font-size: 12.5px; line-height: 14.5px; color: var(--ink); }
  .study-divider { position: absolute; left: 588px; top: 177px; width: 574px; height: 1px; background: #9a9a9a; }

  .topic { position: absolute; width: 201px; }
  .topic-title { font-size: 15px; font-weight: 400; color: var(--navy); white-space: nowrap; }
  .topic-text { margin-top: 10px; font-size: 8px; line-height: 10px; color: var(--ink); }
  .topic-rule { margin-top: 17px; height: 1px; background: #8a8a8a; }

  /* Testimonials header */
  .band { left: 0; top: 1046px; width: 1200px; height: 5px; background: var(--navy); }
  .voices { left: 0; top: 1051px; width: 1200px; height: 149px; background: var(--page); }
  .voices-title { position: absolute; top: 36px; width: 100%; text-align: center; font-size: 26px; font-weight: 400; color: var(--ink); }
  .voices-rule { position: absolute; left: 488px; top: 86px; width: 224px; height: 3px; background: var(--navy); }
  .voices-sub { position: absolute; top: 108px; width: 100%; text-align: center; font-size: 26px; font-weight: 400; color: var(--ink); }
</style>
</head>
<body>

<header class="intro abs">
  <div class="intro-backdrop" role="img" aria-label="Faded photo of a team meeting in a bright office"></div>
  <div class="intro-veil"></div>
  <h1 class="intro-title">A few things we’re great at</h1>
  <div class="intro-rule"></div>
  <p class="intro-text">Lorem Ipsum is simply dummy text of the printing and typesetting industry.<br>Lorem Ipsum has been the industry's standard dummy text ever since the 1500s,<br>when an unknown printer took a galley of type and scrambled it to make a type specimen book.</p>
</header>

<section class="features abs">
  <article class="feature-card">
    <div class="feature-photo" role="img" aria-label="Photo of two colleagues talking at a desk"></div>
    <h2 class="feature-title">Responsive Courses</h2>
    <p class="feature-text">Lorem Ipsum is simply dummy text of the printing and typesetting industry. Lorem Ipsum has been the industry's standard dummy text ever since the 1500s, when an unknown printer took a galley of type and scrambled it to make a type specimen book. It has survived not only five centuries, but also the leap into electronic typesetting, remaining essentially unchanged. It was popularised in the 1960s with the release of Pressmark sheets containing Lorem Ipsum passages, and more recently with desktop publishing software like Folio LayoutDesk including versions of Lorem Ipsum.</p>
    <div class="feature-rule"></div>
    <a class="read-more" href="#">read more&thinsp;&gt;</a>
  </article>
  <article class="feature-card">
    <div class="feature-photo" role="img" aria-label="Photo of a presenter speaking to a meeting table"></div>
    <h2 class="feature-title">Responsive Courses</h2>
    <p class="feature-text">Lorem Ipsum is simply dummy text of the printing and typesetting industry. Lorem Ipsum has been the industry's standard dummy text ever since the 1500s, when an unknown printer took a galley of type and scrambled it to make a type specimen book. It has survived not only five centuries, but also the leap into electronic typesetting, remaining essentially unchanged. It was popularised in the 1960s with the release of Pressmark sheets containing Lorem Ipsum passages, and more recently with desktop publishing software like Folio LayoutDesk including versions of Lorem Ipsum.</p>
    <div class="feature-rule"></div>
    <a class="read-more" href="#">read more&thinsp;&gt;</a>
  </article>
  <article class="feature-card">
    <div class="feature-photo" role="img" aria-label="Photo of a business team seated with laptops"></div>
    <h2 class="feature-title">Responsive Courses</h2>
    <p class="feature-text">Lorem Ipsum is simply dummy text of the printing and typesetting industry. Lorem Ipsum has been the industry's standard dummy text ever since the 1500s, when an unknown printer took a galley of type and scrambled it to make a type specimen book. It has survived not only five centuries, but also the leap into electronic typesetting, remaining essentially unchanged. It was popularised in the 1960s with the release of Pressmark sheets containing Lorem Ipsum passages, and more recently with desktop publishing software like Folio LayoutDesk including versions of Lorem Ipsum.</p>
    <div class="feature-rule"></div>
    <a class="read-more" href="#">read more&thinsp;&gt;</a>
  </article>
</section>

<section class="study abs">
  <div class="trial-panel">
    <div class="trial-veil" role="img" aria-label="Photo of a business team around a laptop in an office"></div>
    <h2 class="trial-title">Set this title from the<br>cusomizer.</h2>
    <div class="trial-rule"></div>
    <a class="trial-button" href="#">Start Free Trial</a>
  </div>

  <div class="study-kicker">COURSES STUDY</div>
  <h3 class="study-title">The Secret of Courses</h3>
  <div class="study-rule"></div>
  <p class="study-text">Lorem Ipsum is simply dummy text of the printing and typesetting industry.<br>Lorem Ipsum has been the industry's standard dummy text ever since the 1500s,<br>when an unknown printer took a galley of type and scrambled it to make a type specimen book.</p>
  <div class="study-divider"></div>

  <div class="topic" style="left:589px; top:192px;">
    <div class="topic-title">How to get the clients</div>
    <p class="topic-text">Lorem Ipsum is simply dummy text of the printing and typesetting industry.</p>
    <div class="topic-rule"></div>
  </div>
  <div class="topic" style="left:844px; top:192px;">
    <div class="topic-title">How to price your services</div>
    <p class="topic-text">Lorem Ipsum is simply dummy text of the printing and typesetting industry.</p>
    <div class="topic-rule"></div>
  </div>
  <div class="topic" style="left:589px; top:269px;">
    <div class="topic-title">How to get paid for your work</div>
    <p class="topic-text">Lorem Ipsum is simply dummy text of the printing and typesetting industry.</p>
    <div class="topic-rule"></div>
  </div>
  <div class="topic" style="left:844px; top:269px;">
    <div class="topic-title">How to grow your business</div>
    <p class="topic-text">Lorem Ipsum is simply dummy text of the printing and typesetting industry.</p>
    <div class="topic-rule"></div>
  </div>
  <div class="topic" style="left:589px; top:341px;">
    <div class="topic-title">How to start with no money</div>
    <p class="topic-text">Lorem Ipsum is simply dummy text of the printing and typesetting industry.</p>
  </div>
  <div class="topic" style="left:844px; top:341px;">
    <div class="topic-title">Plus much more</div>
    <p class="topic-text">Lorem Ipsum is simply dummy text of the printing and typesetting industry.</p>
  </div>
</section>

<div class="band abs"></div>

<section class="voices abs">
  <h2 class="voices-title">People are saying on Chatterly</h2>
  <div class="voices-rule"></div>
  <p class="voices-sub">Don’t take our word for it - here’s what our Learning say :</p>
</section>

</body>
</html>
```